Ghost Tour and Pub Crawl Rack Card Brochure

We are looking to get an updated design for our rack cards that are printed on 4x9 vertical cards. We have uploaded our logo and our previous design. We are looking for a new idea. We need something that jumps out at you when they are printed and sitting next to a group of 50 other brochures. It needs to have all of the must haves incorporated.

Target Market(s)

Women

Industry/Entity Type

Tourism

Font styles to use
Serif
Sans Serif
Decorative
Script
Other font styles liked:
• Doesn't Matter

Colors

Designer to choose colors to be used in the design.

Requirements
Must have
• Needs to be a design that jumps out at you when you are looking at 50 of these in a rack from all different companies.
• 1. Instead of it being just Ghost Tour Pub Crawl, we would like it to have some sort of design that is Ghost Tours and Pub Crawls.
• 2. Our Website must be prominent www.DuskWanderers.com
• 2. We want a box for text at the bottom that we can add a promo code ourselves to the design, so just something that we can edit later that allows us to have enough space to write a promo code, city name, and alternate phone number.
• 3. We want it to say save 10% instead of $5.00
• 4. Phone number 1-8-Lamp-Walk listed on the card
Nice to have
• Needs to be Spooky, but stand out.

```html
<!DOCTYPE html>
<html lang="en">
<head>
<meta charset="utf-8">
<title>Ghost Tour Pub Crawl Rack Card</title>
<link href="https://fonts.googleapis.com/css2?family=Creepster&family=Special+Elite&family=Courier+Prime:wght@700&display=swap" rel="stylesheet">
<style>
  :root {
    --stage: #8a8894;
    --stage-light: #b7b5bd;
    --amber: #f39a2c;
    --amber-deep: #e0701e;
    --ember: #b4440f;
    --embers-dark: #3a1406;
    --night: #050302;
    --ink: #140806;
    --bone: #ffffff;
    --cream: #f3ece2;
  }
  * { margin: 0; padding: 0; box-sizing: border-box; }
  html, body { width: 1200px; height: 750px; overflow: hidden; }
  body {
    background: radial-gradient(ellipse at 50% 40%, var(--stage-light), var(--stage));
    display: flex; align-items: center; justify-content: center;
  }
  .rack-card {
    position: relative;
    width: 300px; height: 675px;
    background: linear-gradient(180deg,
      var(--amber) 0%, var(--amber) 20%,
      var(--amber-deep) 38%, var(--ember) 50%,
      var(--embers-dark) 56%, var(--night) 60%, var(--night) 100%);
    box-shadow: 0 10px 30px rgba(0,0,0,.35);
    overflow: hidden;
    text-align: center;
    color: var(--bone);
  }
  .title {
    position: absolute; top: 22px; left: 0; right: 0;
    font-family: "Creepster", cursive;
    font-size: 62px; line-height: 1; letter-spacing: 1px;
    color: var(--ink);
  }
  .subtitle {
    position: absolute; top: 88px; left: 0; right: 0;
    font-family: "Courier Prime", monospace; font-weight: 700;
    font-size: 26px; line-height: 1; color: var(--ink);
  }
  .offer-word {
    position: absolute; top: 136px; left: 0; right: 0;
    font-family: "Special Elite", monospace;
    font-size: 52px; letter-spacing: 8px; line-height: 1;
  }
  .offer-value {
    position: absolute; top: 184px; left: 0; right: 0;
    font-family: "Special Elite", monospace;
    font-size: 100px; line-height: 1;
  }
  .skyline {
    position: absolute; top: 282px; left: 0;
    width: 300px; height: 110px;
  }
  .brand {
    position: absolute; top: 400px; left: 0; right: 0;
    display: flex; align-items: center; justify-content: center; gap: 8px;
    font-family: "Special Elite", monospace; font-size: 30px; line-height: 1;
  }
  .brand-dot { width: 12px; height: 12px; border-radius: 50%; background: var(--bone); }
  .promo-box {
    position: absolute; top: 458px; left: 0; right: 0;
    font-family: "Special Elite", monospace; font-size: 17px; line-height: 36px;
    color: var(--cream);
  }
  .graveyard {
    position: absolute; top: 536px; left: 0;
    width: 300px; height: 52px;
  }
  .contact {
    position: absolute; top: 594px; left: 0; right: 0;
    font-family: "Special Elite", monospace;
    color: var(--bone);
  }
  .contact-web { font-size: 20px; line-height: 32px; font-weight: 700; letter-spacing: .3px; }
  .contact-phone { font-size: 17px; line-height: 30px; color: var(--cream); }
</style>
</head>
<body>
  <main class="rack-card">
    <h1 class="title">GHOST TOUR</h1>
    <p class="subtitle">PUB CRAWL</p>
    <p class="offer-word">save</p>
    <p class="offer-value">10%</p>

    <svg class="skyline" role="img" aria-label="Haunted castle, bare trees, bats and jack-o-lanterns in silhouette at dusk" viewBox="0 0 300 110" preserveAspectRatio="none">
      <defs>
        <linearGradient id="skyline-tone" x1="0" y1="0" x2="0" y2="1">
          <stop offset="0" stop-color="#2a0d05"/>
          <stop offset="1" stop-color="#050302"/>
        </linearGradient>
      </defs>
      <path d="M0 40 Q75 8 150 46 T300 30 L300 110 L0 110 Z" fill="url(#skyline-tone)"/>
    </svg>

    <div class="brand"><span class="brand-dot"></span><span>Dusk Wanderers</span></div>

    <div class="promo-box">
      <p>city name : Lorem Ipsum</p>
      <p>promo code : 00000</p>
    </div>

    <svg class="graveyard" role="img" aria-label="Graveyard silhouette with crosses and pumpkins against an ember glow" viewBox="0 0 300 52" preserveAspectRatio="none">
      <defs>
        <linearGradient id="grave-glow" x1="0" y1="0" x2="0" y2="1">
          <stop offset="0" stop-color="#5a2008"/>
          <stop offset="0.5" stop-color="#2a0d05"/>
          <stop offset="1" stop-color="#050302"/>
        </linearGradient>
      </defs>
      <path d="M0 14 Q150 0 300 14 L300 52 L0 52 Z" fill="url(#grave-glow)"/>
    </svg>

    <div class="contact">
      <p class="contact-web">www.DuskWanderers.com</p>
      <p class="contact-phone">Call us 1-8-Lamp-Walk</p>
    </div>
  </main>
</body>
</html>
```